Simple elegant business card

General card for a fin and television director.
Just want name, email, phone and address.

Target Market(s)

Prospective employers

Industry/Entity Type

Business

Requirements
Must have
• As above
Nice to have
• Logo but not necessary.
Should not have
• Not too colourful or funky.
• Simplicity and elegance the way to go.

```html
<!DOCTYPE html>
<html lang="en">
<head>
<meta charset="utf-8">
<title>Nora Hale – Business Card</title>
<link rel="stylesheet" href="https://fonts.googleapis.com/css2?family=Arimo:wght@400;700&display=swap">
<style>
  :root {
    --navy-deep: #06142b;
    --navy: #0c1f3d;
    --navy-mid: #142a48;
    --name-white: #ffffff;
    --detail-grey: #b9c0cc;
    --beam: #e8ecf2;
  }
  html, body {
    margin: 0;
    padding: 0;
    width: 1200px;
    height: 668px;
    overflow: hidden;
    background: var(--navy-deep);
  }
  .card {
    position: relative;
    width: 1200px;
    height: 668px;
    overflow: hidden;
    background:
      radial-gradient(ellipse 900px 600px at 70% 30%, var(--navy-mid) 0%, var(--navy) 45%, var(--navy-deep) 100%);
    font-family: "Arimo", "Helvetica Neue", Helvetica, Arial, sans-serif;
  }
  .light-beam {
    position: absolute;
    inset: 0;
    width: 1200px;
    height: 668px;
  }
  .identity {
    position: absolute;
    left: 95px;
    top: 336px;
  }
  .identity__name {
    margin: 0 0 44px;
    font-size: 51px;
    font-weight: 700;
    letter-spacing: -0.3px;
    color: var(--name-white);
    line-height: 1;
  }
  .identity__contact {
    margin: 0;
    font-style: normal;
    font-size: 38px;
    font-weight: 400;
    line-height: 52px;
    color: var(--detail-grey);
  }
  .identity__contact span { display: block; }
</style>
</head>
<body>
  <main class="card">
    <svg class="light-beam" viewBox="0 0 1200 668" aria-hidden="true">
      <defs>
        <filter id="beam-soft" x="-50%" y="-50%" width="200%" height="200%">
          <feGaussianBlur stdDeviation="40"/>
        </filter>
        <filter id="beam-core-soft" x="-50%" y="-50%" width="200%" height="200%">
          <feGaussianBlur stdDeviation="22"/>
        </filter>
        <linearGradient id="beam-fade" x1="1" y1="0" x2="0" y2="0">
          <stop offset="0" stop-color="var(--beam)" stop-opacity="0.55"/>
          <stop offset="0.35" stop-color="var(--beam)" stop-opacity="0.25"/>
          <stop offset="1" stop-color="var(--beam)" stop-opacity="0"/>
        </linearGradient>
        <linearGradient id="beam-core-fade" x1="1" y1="0" x2="0" y2="0">
          <stop offset="0" stop-color="var(--beam)" stop-opacity="0.75"/>
          <stop offset="0.5" stop-color="var(--beam)" stop-opacity="0.2"/>
          <stop offset="1" stop-color="var(--beam)" stop-opacity="0"/>
        </linearGradient>
      </defs>
      <g transform="rotate(-21 1150 170)">
        <ellipse cx="900" cy="200" rx="480" ry="120" fill="url(#beam-fade)" filter="url(#beam-soft)"/>
        <ellipse cx="1080" cy="180" rx="230" ry="55" fill="url(#beam-core-fade)" filter="url(#beam-core-soft)"/>
      </g>
    </svg>

    <section class="identity">
      <h1 class="identity__name">Nora Hale</h1>
      <address class="identity__contact">
        <span class="identity__email">norahale@mail.com</span>
        <span class="identity__phone">+1 310 555 0142</span>
      </address>
    </section>
  </main>
</body>
</html>
```